Stationery for tax services company
Ledger Harbor Advisors
Stationery for tax services company - Financial Services
Creative Brief
Simple
Colin T. Westbrook, EA, JD, MST
President
4817 North Palomar Avenue, Suite 6 Honolulu, HI 96814
fileclearhelp@mailvora.net
www.LedgerHarborAdvisors.net
I also need business cards for the 2 following people: [Beth Colton, EA / Tax Preparer] [Marla Penhurst / Executive Assistant]
We need a design for business cards, letterhead page 1 of 2, letterhead page 2 of 2, envelopes small, label for large envelopes, fax cover sheet, email signature, and presentation folders.

```html
<!DOCTYPE html>
<html lang="en">
<head>
<meta charset="utf-8">
<title>Ledger Harbor Advisors — Stationery</title>
<link href="https://fonts.googleapis.com/css2?family=Libre+Baskerville&family=Open+Sans:wght@400;600&display=swap" rel="stylesheet">
<style>
:root{
  --board:#e9dfcf;
  --paper:#ffffff;
  --navy:#2a2d6b;
  --blue:#3a3f9a;
  --deep:#1d1f52;
  --grey:#7d7f87;
  --soft:#d9dae0;
  --faint:#eeeef3;
  --label:#6d6458;
}
*{margin:0;padding:0;box-sizing:border-box}
html,body{width:1200px;height:446px;overflow:hidden}
body{background:var(--board);font-family:"Open Sans",sans-serif;color:var(--navy);position:relative}
.label{position:absolute;font-size:6px;letter-spacing:1px;text-transform:uppercase;color:var(--label)}
.sheet{position:absolute;background:var(--paper);box-shadow:0 1px 4px rgba(0,0,0,.18)}
.brand{display:flex;align-items:center;gap:5px;font-family:"Libre Baskerville",serif;color:var(--navy);white-space:nowrap}
.brand .dot{border-radius:50%;background:var(--navy);flex:none}
.faint-mark{position:absolute;border-radius:50%;background:var(--faint)}
.contact-list{position:absolute;list-style:none;font-size:4.5px;color:var(--grey);line-height:7px}
.contact-list li::before{content:"";display:inline-block;width:4px;height:4px;background:var(--blue);margin-right:3px;vertical-align:middle}
.footer-line{position:absolute;left:0;right:0;bottom:14px;text-align:center;font-size:4.5px;color:var(--grey)}
.footer-line span{margin:0 4px}
.footer-line span::before{content:"";display:inline-block;width:3.5px;height:3.5px;background:var(--blue);margin-right:2px;vertical-align:middle}

/* business cards */
.card{position:absolute;left:24px;width:122px;height:42px;box-shadow:0 1px 3px rgba(0,0,0,.2)}
.card-front{top:211px;background:var(--paper)}
.card-back{top:269px;background:linear-gradient(135deg,var(--blue),var(--deep))}
.card-front .brand{position:absolute;left:10px;top:8px;font-size:7px}
.card-front .person{position:absolute;left:10px;bottom:6px;font-size:3.8px;color:var(--grey);line-height:5px}
.card-back .faint-mark{left:30px;top:4px;width:62px;height:34px;border-radius:50%;background:rgba(255,255,255,.08)}

/* letterheads */
.letterhead{top:19px;width:269px;height:394px}
.lh-one{left:175px}
.lh-two{left:473px}
.letterhead .brand{position:absolute;left:22px;top:20px;font-size:11px}
.letterhead .faint-mark{left:60px;top:225px;width:150px;height:110px}
.lh-one .contact-list{left:178px;top:16px}

/* envelopes */
.env{position:absolute;left:852px;width:336px;height:89px}
.env-back{top:19px;background:linear-gradient(180deg,var(--blue),var(--deep))}
.env-grey{top:101px;background:var(--paper)}
.env-grey .flap{position:absolute;inset:0 0 30px 0;background:linear-gradient(180deg,#9a9ca5,#6e7079);clip-path:polygon(0 0,100% 0,100% 60%,50% 100%,0 60%)}
.env-grey .brand{position:absolute;left:150px;top:40px;font-size:6px}
.env-white{top:187px;background:var(--paper)}
.env-white .flap{position:absolute;inset:0 0 30px 0;background:#f1f1f4;clip-path:polygon(0 0,100% 0,100% 60%,50% 100%,0 60%);border-bottom:1px solid var(--soft)}
.env-front{position:absolute;left:799px;top:276px;width:360px;height:137px}
.env-front .brand{position:absolute;left:16px;top:16px;font-size:9px}
.env-front .return{position:absolute;left:16px;top:32px;font-size:4.5px;color:var(--grey)}
.env-front .faint-mark{right:20px;bottom:12px;width:80px;height:55px}
</style>
</head>
<body>

<div class="label" style="left:24px;top:192px">Business Cards</div>
<div class="card card-front">
  <div class="brand"><span class="dot" style="width:6px;height:6px"></span>Ledger Harbor Advisors</div>
  <div class="person">Colin T. Westbrook, EA, JD, MST<br>fileclearhelp@mailvora.net</div>
</div>
<div class="label" style="left:24px;top:257px">Business Card Front</div>
<div class="card card-back"><div class="faint-mark"></div></div>
<div class="label" style="left:24px;top:316px">Business Card Back</div>

<div class="sheet letterhead lh-one">
  <div class="brand"><span class="dot" style="width:9px;height:9px"></span>Ledger Harbor Advisors</div>
  <ul class="contact-list">
    <li>4817 North Palomar Avenue</li>
    <li>Suite 6, Honolulu, HI 96814</li>
    <li>(808) 555-0142</li>
    <li>fileclearhelp@mailvora.net</li>
    <li>www.LedgerHarborAdvisors.net</li>
  </ul>
  <div class="faint-mark"></div>
</div>
<div class="label" style="left:270px;top:424px">Letterhead Option 1</div>

<div class="sheet letterhead lh-two">
  <div class="brand"><span class="dot" style="width:9px;height:9px"></span>Ledger Harbor Advisors</div>
  <div class="faint-mark"></div>
  <div class="footer-line"><span>4817 North Palomar Avenue, Suite 6</span><span>(808) 555-0142</span><span>fileclearhelp@mailvora.net</span><span>www.LedgerHarborAdvisors.net</span></div>
</div>
<div class="label" style="left:570px;top:424px">Letterhead Option 2</div>

<div class="sheet env env-back"></div>
<div class="sheet env env-grey"><div class="flap"></div><div class="brand"><span class="dot" style="width:5px;height:5px"></span>Ledger Harbor Advisors</div></div>
<div class="sheet env env-white"><div class="flap"></div></div>
<div class="sheet env-front">
  <div class="brand"><span class="dot" style="width:7px;height:7px"></span>Ledger Harbor Advisors</div>
  <div class="return">4817 North Palomar Avenue, Suite 6 Honolulu, HI 96814</div>
  <div class="faint-mark"></div>
</div>
<div class="label" style="left:950px;top:424px">Envelope Design</div>

</body>
</html>
```